snugSEAL - packaging design for plastic zip-lock mechansim

Looking for packaging designs for my patented product, which provides the ability to lock and close existing plastic bags, which have been opened up (like sugar or flour bag, snack bag, etc.). With applying snugSEAL to any bag once opened, the products can be held safe, locked and dry.
Please check my supporting documentation attached, including logos and packaging description.
The packaging design has to make clear to the customer:
- WHAT is this product for
- how to USA
- what are the BENEFITS and the VALUE
I am looking for a long term cooperation with the winning designer, as I will need multiple variations of the packaging depending on individual product usage. I am thinking of approximately 10 different variations in the future.
Updates
Project Deadline Extended Reason: Extending deadline to receive more designs. Please submit your designs according to my description. Let me know if any questions!This will be a long term cooperation as I will need subsequent designs for alternative product variations in the future. Added Saturday, October 22, 2016
Target Market(s)
All consumers who buy products in the supermarket. In particular when they buy products in bags (like salt, sugar, flour, detergents, snacks, ...)
Industry/Entity Type
Retail
Look and feel
Each slider illustrates characteristics of the customer's brand and the style your logo design should communicate.

```html
<!DOCTYPE html>
<html lang="en">
<head>
<meta charset="utf-8">
<title>snugSEAL – Plastic Extension packaging</title>
<link rel="stylesheet" href="https://fonts.googleapis.com/css2?family=Open+Sans:ital,wght@0,400;0,600;0,700;1,700;1,800&display=swap">
<style>
  :root {
    --navy: #0c3466;
    --navy-deep: #082a55;
    --blue: #1f6fd0;
    --blue-light: #5aa2ee;
    --sky: #9cc7f5;
    --yellow: #f5e51a;
    --white: #ffffff;
    --ink: #1d2430;
    --stage: #e9e9e9;
    --photo-light: #eef3f8;
    --photo-mid: #cfdbe8;
  }
  * { box-sizing: border-box; margin: 0; padding: 0; }
  html, body { width: 1200px; height: 1000px; overflow: hidden; }
  body {
    background: radial-gradient(ellipse at center, #f7f7f7 0%, var(--stage) 60%, #d9d9d9 100%);
    font-family: "Open Sans", Arial, sans-serif;
    position: relative;
  }
  .dieline {
    position: absolute; left: 80px; top: 205px; width: 1040px;
    box-shadow: 0 10px 30px rgba(0,0,0,.18);
  }

  /* Front panel */
  .front {
    position: relative; height: 270px; display: flex;
    background: radial-gradient(circle at 72% 35%, var(--blue-light) 0%, var(--blue) 45%, #1354ad 100%);
    overflow: hidden;
  }
  .brand-strip {
    width: 120px; background: var(--navy); position: relative;
    border-right: 3px solid var(--sky);
  }
  .brand-strip .brand {
    position: absolute; left: 50%; top: 50%;
    transform: translate(-50%, -50%) rotate(-90deg);
    font-size: 34px; font-weight: 400; color: var(--white); letter-spacing: 1px; white-space: nowrap;
  }
  .front-body { position: relative; flex: 1; }
  .title {
    position: absolute; left: 40px; top: 18px;
    font-style: italic; font-weight: 800; color: var(--white);
    font-size: 58px; line-height: 54px; letter-spacing: -1px;
    text-shadow: 2px 3px 4px rgba(0,0,0,.35);
  }
  .title .line2 { display: block; }
  .subtitle {
    position: absolute; left: 52px; top: 138px;
    font-style: italic; font-weight: 800; color: var(--yellow); font-size: 27px;
    text-shadow: 1px 2px 3px rgba(0,0,0,.35);
  }
  .size {
    position: absolute; left: 56px; top: 212px;
    font-style: italic; font-weight: 700; color: var(--white); font-size: 14px;
  }
  .product-photo {
    position: absolute; right: 0; top: 15px; width: 400px; height: 165px;
    background: linear-gradient(170deg, var(--photo-light) 0%, var(--photo-mid) 100%);
  }
  .strap-photo {
    position: absolute; left: 450px; top: 125px; width: 70px; height: 22px;
    background: linear-gradient(var(--photo-light), var(--photo-mid));
  }
  .bag-photo {
    position: absolute; left: 445px; top: 165px; width: 75px; height: 85px;
    background: linear-gradient(160deg, var(--photo-light), var(--photo-mid));
  }
  .stand-stick {
    position: absolute; left: 540px; top: 205px; width: 225px; height: 58px;
    background: rgba(8,42,85,.55); color: var(--white); text-align: center; padding-top: 4px;
    font-style: italic;
  }
  .stand-stick strong { display: block; font-weight: 800; font-size: 16px; }
  .stand-stick span { display: block; font-size: 12px; line-height: 14px; font-weight: 700; }
  .count {
    position: absolute; right: 20px; top: 180px; text-align: center;
    font-style: italic; font-weight: 800; line-height: 1;
  }
  .count .num { display: block; color: var(--yellow); font-size: 48px; text-shadow: 1px 2px 3px rgba(0,0,0,.4); }
  .count .unit { display: block; color: var(--white); font-size: 26px; }

  /* Bands */
  .band {
    height: 52px; background: var(--navy); color: var(--white);
    display: flex; align-items: center; border-top: 2px solid var(--blue);
  }
  .band .brand { width: 360px; text-align: center; font-size: 22px; letter-spacing: 1px; }
  .band .label { flex: 1; text-align: center; font-size: 18px; font-weight: 600; letter-spacing: 1px; }
  .band.flipped { transform: rotate(180deg); height: 58px; border-top: 0; border-bottom: 6px solid var(--blue); }

  /* Back panel */
  .back {
    height: 205px; background: var(--white); display: flex; padding: 12px 36px 0;
    border-bottom: 8px solid var(--blue);
  }
  .column { width: 380px; font-size: 12.5px; line-height: 15px; color: var(--ink); }
  .column h2 { font-size: 14px; font-weight: 700; color: var(--navy); margin-bottom: 8px; }
  .column h3 { font-size: 12.5px; font-weight: 700; margin-bottom: 6px; }
  .column ul { list-style: none; }
  .column li { position: relative; padding-left: 8px; margin-bottom: 8px; }
  .column li::before { content: "•"; position: absolute; left: -2px; color: var(--navy); }
  .diagram {
    width: 210px; height: 180px; margin: 0 30px 0 40px;
    background: linear-gradient(#eef3fa, #f8fafc); border: 1px solid #c7d3e6;
  }
</style>
</head>
<body>
  <main class="dieline">
    <section class="front">
      <div class="brand-strip"><span class="brand">snugSEAL</span></div>
      <div class="front-body">
        <h1 class="title">Plastic<span class="line2">Extension</span></h1>
        <p class="subtitle">ZIP LOCK MECHANISM</p>
        <p class="size">10 STRAP 10 in x 0 in (25cm x 00cm</p>
        <div class="product-photo" role="img" aria-label="Photo of a clear zip-lock strap close up"></div>
        <div class="strap-photo" role="img" aria-label="Small photo of a zip strap"></div>
        <div class="bag-photo" role="img" aria-label="Small photo of a plastic bag"></div>
        <div class="stand-stick">
          <strong>STAND &amp; STICK</strong>
          <span>stick to your existing</span>
          <span>plastic or paper bag easily</span>
        </div>
        <div class="count"><span class="num">10</span><span class="unit">STRAPS</span></div>
      </div>
    </section>

    <div class="band"><span class="brand">snugSEAL</span><span class="label">ZIP LOCK MECHANISM</span></div>

    <section class="back">
      <div class="column">
        <h2>HOW DOES IT WORK:</h2>
        <ul>
          <li>Just remove the protection foil from the adhesive surface on both inner sides of the product,</li>
          <li>And then simply stick and attach it to any bag (snacks, vegetables, flour, sugar) to close it safely once opened (and when there is not any other closing mechanism existing)</li>
          <li>The straps have a length of approx. 25 cm, so they can close even big bags.</li>
        </ul>
      </div>
      <div class="diagram" role="img" aria-label="Line drawing showing the strap stuck onto an existing bag"></div>
      <div class="column">
        <h3>For SMALLER BAGS</h3>
        <ul>
          <li>Just simply cut off the strap with scissors.</li>
          <li>In case you will cut off the strap which includes the slider, there will be a little plastic clip delivered with the product, to be stick at the end of the slider bar, so that the slider itself cannot move out.</li>
          <li>The clip is part of the slider based product.</li>
          <li>It's a little small tiny plastic piece, which will be attached over the slider bar, at the end of the strap.</li>
        </ul>
      </div>
    </section>

    <div class="band flipped"><span class="brand">snugSEAL</span><span class="label">ZIP LOCK MECHANISM</span></div>
  </main>
</body>
</html>
```